Morvela Aesthetic Doctor

I require an elegant, luxurious looking business card for my aesthetic business. I am a doctor and that will set me aside from competitors. I am planning to provide home and spa based treatments to clients with high expectations. I have attached my logo.

```html
<!DOCTYPE html>
<html lang="en">
<head>
<meta charset="utf-8">
<title>Morvela Aesthetic Doctor — Business Card</title>
<link href="https://fonts.googleapis.com/css2?family=Open+Sans:wght@400;600;700&display=swap" rel="stylesheet">
<style>
  :root {
    --backdrop: #3b3b3d;
    --card-black: #1c1c1e;
    --sky: #55b4ea;
    --sky-deep: #3f97d6;
    --silver: #aab4c4;
    --white: #ffffff;
  }
  * { margin: 0; padding: 0; box-sizing: border-box; }
  html, body { width: 799px; height: 1200px; overflow: hidden; }
  body {
    background: var(--backdrop);
    font-family: "Open Sans", Arial, sans-serif;
    position: relative;
  }
  .card {
    position: absolute;
    left: 50px;
    width: 700px;
    height: 400px;
    background: var(--card-black);
    border-radius: 4px;
    overflow: hidden;
    box-shadow: 0 12px 30px rgba(0,0,0,.45);
  }
  .card-front { top: 90px; }
  .card-back { top: 690px; }

  /* Brand lockup */
  .brand { position: absolute; display: flex; align-items: center; gap: 18px; }
  .brand-dot {
    width: 74px; height: 74px; border-radius: 50%;
    background: var(--sky);
    flex: none;
  }
  .brand-name {
    color: var(--sky);
    font-weight: 600;
    line-height: 1.05;
    letter-spacing: 2px;
    text-transform: uppercase;
  }
  .brand-name .main { display: block; font-size: 46px; letter-spacing: 4px; }
  .brand-name .sub { display: block; font-size: 20px; }
  .card-front .brand { left: 150px; top: 52px; }

  /* Front */
  .top-stripe {
    position: absolute; left: 0; right: 0; top: 200px; height: 14px;
    background: var(--sky);
  }
  .services {
    position: absolute; left: 0; right: 0; top: 230px;
    text-align: center; color: var(--white);
    font-size: 19px; line-height: 1.45;
  }
  .services .sep { margin: 0 12px; }
  .tagline-band {
    position: absolute; left: 0; right: 0; top: 302px; height: 46px;
    background: var(--sky);
    color: var(--white);
    font-size: 21px; letter-spacing: 1px;
    display: flex; align-items: center; justify-content: center;
    text-transform: uppercase;
  }

  /* Back */
  .back-shape { position: absolute; inset: 0; }
  .card-back .brand {
    left: 36px; top: 100px; width: 230px;
    flex-direction: column; align-items: center; gap: 12px;
    text-align: center;
  }
  .card-back .brand-dot { width: 70px; height: 70px; }
  .card-back .brand-name .main { font-size: 38px; letter-spacing: 3px; }
  .card-back .brand-name .sub { font-size: 16px; letter-spacing: 1.5px; }
  .contact {
    position: absolute; left: 400px; top: 80px;
    color: var(--white);
  }
  .contact-name { font-size: 24px; font-weight: 700; }
  .contact-name .creds { font-size: 14px; font-weight: 400; margin-left: 6px; }
  .contact-title { font-size: 17px; line-height: 1.3; margin-top: 2px; }
  .contact-list { list-style: none; margin-top: 22px; font-size: 18px; line-height: 1.75; }
  .contact-list li { display: flex; align-items: center; gap: 12px; }
  .contact-list svg { width: 16px; height: 16px; fill: var(--white); flex: none; }
  .follow { display: flex; align-items: center; gap: 10px; font-size: 18px; margin-top: 2px; }
  .follow .social { width: 20px; height: 20px; border-radius: 50%; background: var(--white); }
</style>
</head>
<body>

  <section class="card card-front">
    <div class="brand">
      <span class="brand-dot"></span>
      <div class="brand-name"><span class="main">Morvela</span><span class="sub">Aesthetic Doctor</span></div>
    </div>
    <div class="top-stripe"></div>
    <p class="services">
      Dermal Injectables<span class="sep">|</span>Plasma Facials<span class="sep">|</span>Microneedling<br>
      Skin Boosters<span class="sep">|</span>Excessive Sweating
    </p>
    <div class="tagline-band">Home and Spa Based Treatments</div>
  </section>

  <section class="card card-back">
    <svg class="back-shape" viewBox="0 0 700 400" preserveAspectRatio="none">
      <defs>
        <linearGradient id="panelBlue" x1="0" y1="0" x2="0" y2="1">
          <stop offset="0" stop-color="#5cbaed"/>
          <stop offset="1" stop-color="#3f97d6"/>
        </linearGradient>
      </defs>
      <path d="M360 0 C 350 160, 300 310, 120 400 L 700 400 L 700 0 Z" fill="#aab4c4"/>
      <path d="M374 0 C 364 160, 318 312, 144 400 L 700 400 L 700 0 Z" fill="url(#panelBlue)"/>
    </svg>
    <div class="brand">
      <span class="brand-dot"></span>
      <div class="brand-name"><span class="main">Morvela</span><span class="sub">Aesthetic Doctor</span></div>
    </div>
    <div class="contact">
      <div class="contact-name">Dr Lena Voss<span class="creds">MRCPCH MD</span></div>
      <div class="contact-title">Australasian Diploma<br>of Aesthetic Medicine</div>
      <ul class="contact-list">
        <li><svg viewBox="0 0 24 24"><path d="M6.6 10.8a15 15 0 006.6 6.6l2.2-2.2a1 1 0 011-.25 11.4 11.4 0 003.6.57 1 1 0 011 1V20a1 1 0 01-1 1A17 17 0 013 4a1 1 0 011-1h3.5a1 1 0 011 1c0 1.25.2 2.45.57 3.57a1 1 0 01-.25 1z"/></svg>0800 555 019</li>
        <li><svg viewBox="0 0 24 24"><path d="M2 5h20v14H2z M2 5l10 8 10-8" fill="none" stroke="#fff" stroke-width="2"/></svg>lena@morvela.co.nz</li>
        <li><svg viewBox="0 0 24 24"><circle cx="12" cy="12" r="9" fill="none" stroke="#fff" stroke-width="2"/><path d="M3 12h18M12 3c3 3 3 15 0 18M12 3c-3 3-3 15 0 18" fill="none" stroke="#fff" stroke-width="1.6"/></svg>www.morvela.co.nz</li>
      </ul>
      <div class="follow">Follow us on: <span class="social"></span><span class="social"></span></div>
    </div>
  </section>

</body>
</html>
```